" Uma empresa que funcionará em sua maior parte para o B2B ,onde motoristas que não tem veículos para trabalhar,contratam para ir ao mercado de trabalho e alugar frotas pra empresas "

```html
<!DOCTYPE html>
<html lang="pt-BR">
<head>
<meta charset="UTF-8">
<title>Rotta Locadora de Veículos — Papelaria</title>
<link href="https://fonts.googleapis.com/css2?family=Poppins:wght@400;600;700&display=swap" rel="stylesheet">
<style>
  :root {
    --backdrop: #3b3633;
    --envelope: #17748b;
    --flap: #2590ab;
    --flap-edge: #146579;
    --brand: #2a9cbf;
    --sheet: #ffffff;
    --wave-soft: #d7eef5;
    --wave-mid: #a9d9e8;
    --ink-light: #e6f4f8;
  }
  * { margin: 0; padding: 0; box-sizing: border-box; }
  html, body { width: 1200px; height: 1200px; overflow: hidden; }
  body {
    background: var(--backdrop);
    font-family: "Poppins", sans-serif;
    position: relative;
  }
  .envelope {
    position: absolute;
    left: 53px; top: 79px;
    width: 636px; height: 881px;
    background: var(--envelope);
    overflow: hidden;
  }
  .envelope-flap {
    position: absolute; left: 0; top: 0;
    width: 636px; height: 160px;
  }
  .envelope-brand {
    position: absolute; left: 0; top: 62px; width: 100%;
    text-align: center; color: var(--ink-light);
  }
  .envelope-brand .brand-name { font-size: 44px; font-weight: 700; line-height: 1; letter-spacing: -1px; }
  .envelope-brand .brand-tagline { font-size: 10px; font-weight: 600; letter-spacing: 0.4px; margin-top: 1px; }
  .contact-list {
    position: absolute; left: 62px; top: 736px;
    list-style: none; color: var(--ink-light);
    font-size: 9.5px; line-height: 17px;
  }
  .contact-list li { display: flex; align-items: flex-start; gap: 7px; }
  .contact-list .icon { width: 9px; height: 9px; margin-top: 4px; flex: none; }
  .contact-list .indent { padding-left: 16px; }
  .sheet {
    position: absolute;
    left: 533px; top: 312px;
    width: 590px; height: 809px;
    background: var(--sheet);
    overflow: hidden;
    box-shadow: -4px 4px 14px rgba(0,0,0,0.25);
  }
  .sheet-brand {
    position: absolute; left: 0; top: 446px; width: 100%;
    text-align: center; color: var(--brand);
  }
  .sheet-brand .brand-name { font-size: 100px; font-weight: 700; line-height: 1; letter-spacing: -2px; }
  .sheet-brand .brand-tagline { font-size: 20px; font-weight: 600; letter-spacing: 0.4px; margin-top: 2px; }
  .sheet-waves {
    position: absolute; left: 0; top: 612px;
    width: 590px; height: 144px;
    background: linear-gradient(180deg, rgba(255,255,255,0) 0%, var(--wave-soft) 35%, var(--wave-mid) 55%, var(--wave-soft) 75%, rgba(255,255,255,0) 100%);
  }
</style>
</head>
<body>
  <section class="envelope" aria-label="Envelope">
    <svg class="envelope-flap" viewBox="0 0 636 160" preserveAspectRatio="none">
      <path d="M0 0 H636 V128 Q628 146 590 148 Q318 160 46 148 Q8 146 0 128 Z" fill="var(--flap)"/>
      <path d="M0 128 Q8 146 46 148 Q318 160 590 148 Q628 146 636 128" fill="none" stroke="var(--flap-edge)" stroke-width="3"/>
    </svg>
    <div class="envelope-brand">
      <div class="brand-name">rotta</div>
      <div class="brand-tagline">LOCADORA DE VEÍCULOS</div>
    </div>
    <ul class="contact-list">
      <li>
        <svg class="icon" viewBox="0 0 10 10"><path d="M5 0.5a3.2 3.2 0 0 1 3.2 3.2C8.2 6 5 9.5 5 9.5S1.8 6 1.8 3.7A3.2 3.2 0 0 1 5 0.5z" fill="currentColor"/></svg>
        <span>Rua das Frotas, 480 • Centro</span>
      </li>
      <li class="indent">Vale Claro - VC</li>
      <li>
        <svg class="icon" viewBox="0 0 10 10"><path d="M2 0.8l2 2-1 1.2a6 6 0 0 0 3 3l1.2-1 2 2-1.2 1.4C4.5 9.4 0.6 5.5 0.6 2z" fill="currentColor"/></svg>
        <span>(00) 4020-1180</span>
      </li>
      <li>
        <svg class="icon" viewBox="0 0 10 10"><rect x="0.5" y="2" width="9" height="6" fill="none" stroke="currentColor"/><path d="M0.5 2L5 5.5 9.5 2" fill="none" stroke="currentColor"/></svg>
        <span>contato@rottafrotas.com.br</span>
      </li>
      <li>
        <svg class="icon" viewBox="0 0 10 10"><rect x="0.8" y="0.8" width="8.4" height="8.4" rx="2" fill="none" stroke="currentColor"/></svg>
        <span>@rottafrotas</span>
      </li>
      <li>
        <svg class="icon" viewBox="0 0 10 10"><circle cx="5" cy="5" r="4.3" fill="currentColor"/></svg>
        <span>www.rottafrotas.com.br</span>
      </li>
    </ul>
  </section>

  <section class="sheet" aria-label="Folha timbrada">
    <div class="sheet-brand">
      <div class="brand-name">rotta</div>
      <div class="brand-tagline">LOCADORA DE VEÍCULOS</div>
    </div>
    <div class="sheet-waves" role="img" aria-label="Faixa decorativa de linhas onduladas em azul claro"></div>
  </section>
</body>
</html>
```